Diabetic test strips buying business needs business card

Hi all, thanks for picking up my project.

What we do is buy boxes of diabetic test strips from everyday people that are diabetics.

Many diabetes do not test all the time so they tend to have boxes left over.

This creates an opportunity for them to make some extra money by selling the boxes to us.

Here is some of the information i will want on the business card. We do not have a logo.

Name: Brandt / Dwayne
Toll Free : 1-800-555-0142

Call Today and Get Your Cash!

Website: www.glucoswapcorner.com
Email contact@glucoswapcorner.com

We buy diabetic test strips and pay you cash!
We accept many different brands.

Notes:

1 - Print should be readable since some diabetics have poor eyesight

2 - Sorry we do not have a logo

Please ask me any questions you have.

Thanks

Dwayne

I just increase the dollar amount on my business card project.

All, i'm going to decide on the design i think is the best for me today. Please don't submit anymore designs. Thank you all for your time and great designs. Dwayne

Diabetics

Business

• People i would like one sir of the card to be line a mini billboard. Seems like many of the design i'm seeing are very conservative as that my be my fault for not setting the slider bar correctly.

```html
<!DOCTYPE html>
<html lang="en">
<head>
<meta charset="utf-8">
<title>GlucoSwapCorner business card</title>
<link rel="stylesheet" href="https://fonts.googleapis.com/css2?family=Nunito:wght@700;800&family=Questrial&family=Arimo:wght@700&display=swap">
<style>
  :root {
    --page-bg: #ecedec;
    --card-blue: #1b95d8;
    --brand-orange: #ef821f;
    --card-white: #ffffff;
    --ink-dark: #2f2f2f;
    --ink-mid: #3d3d3d;
    --photo-light: #eef6fb;
    --photo-mid: #b9d9ee;
  }
  * { margin: 0; padding: 0; box-sizing: border-box; }
  html, body {
    width: 1003px; height: 1200px; overflow: hidden;
    background: var(--page-bg);
    font-family: "Nunito", Arial, sans-serif;
  }
  .canvas { position: relative; width: 1003px; height: 1200px; }

  .card {
    position: absolute;
    width: 773px; height: 458px;
    border-radius: 26px;
    overflow: hidden;
    box-shadow: 0 4px 14px rgba(0,0,0,0.28);
  }

  /* Front side */
  .card-front { left: 96px; top: 90px; background: var(--card-blue); }
  .front-photo {
    position: absolute; left: 140px; top: 0; width: 560px; height: 340px;
    background: radial-gradient(ellipse 48% 55% at 50% 42%,
      var(--photo-light) 0%, var(--photo-light) 45%, var(--photo-mid) 70%, rgba(27,149,216,0) 100%);
  }
  .front-headline {
    position: absolute; left: 0; right: 0; top: 356px;
    text-align: center; color: var(--card-white);
    font-family: "Nunito", Arial, sans-serif;
    font-size: 40px; font-weight: 800; line-height: 48px; letter-spacing: -0.3px;
  }
  .front-band {
    position: absolute; left: 0; right: 0; bottom: 0; height: 35px;
    background: var(--brand-orange);
  }

  /* Back side */
  .card-back { left: 102px; top: 648px; background: var(--card-blue); }
  .back-top {
    position: absolute; left: 0; top: 0; width: 100%; height: 211px;
    background: var(--card-white);
  }
  .back-rule {
    position: absolute; left: 0; top: 211px; width: 100%; height: 8px;
    background: var(--brand-orange);
  }
  .contact-name {
    position: absolute; left: 146px; top: 60px;
    font-family: "Arimo", Arial, sans-serif;
    font-size: 28px; font-weight: 700; color: var(--ink-dark);
  }
  .contact-line {
    position: absolute; left: 104px;
    display: flex; align-items: center; gap: 12px;
    font-family: "Questrial", Arial, sans-serif;
    font-size: 29px; font-weight: 400; color: var(--ink-mid);
  }
  .contact-web { top: 112px; }
  .contact-mail { top: 154px; }
  .contact-line svg { width: 22px; height: 22px; flex: none; }

  .back-pitch {
    position: absolute; left: 0; right: 0; top: 234px;
    text-align: center; color: var(--card-white);
    font-size: 24px; font-weight: 800; line-height: 32px;
  }
  .call-button {
    position: absolute; left: 190px; top: 315px; width: 396px; height: 118px;
    background: var(--brand-orange); border-radius: 12px;
    color: var(--card-white); text-align: center;
  }
  .call-number {
    margin-top: 14px;
    display: flex; justify-content: center; align-items: center; gap: 8px;
    font-size: 33px; font-weight: 800; line-height: 42px;
  }
  .call-number svg { width: 26px; height: 26px; }
  .call-action { margin-top: 10px; font-size: 23px; font-weight: 800; line-height: 30px; }
</style>
</head>
<body>
<main class="canvas">

  <section class="card card-front">
    <div class="front-photo" role="img" aria-label="Photo of hands using a blood glucose meter with a test strip and lancing pen"></div>
    <h1 class="front-headline">GlucoSwapCorner.com</h1>
    <div class="front-band"></div>
  </section>

  <section class="card card-back">
    <div class="back-top"></div>
    <div class="back-rule"></div>

    <p class="contact-name">Brandt Dwayne</p>
    <p class="contact-line contact-web">
      <svg viewBox="0 0 22 22" aria-hidden="true">
        <g fill="none" stroke="#ef821f" stroke-width="1.6">
          <circle cx="11" cy="11" r="9"/>
          <ellipse cx="11" cy="11" rx="4" ry="9"/>
          <line x1="2" y1="11" x2="20" y2="11"/>
          <line x1="4" y1="6" x2="18" y2="6"/>
          <line x1="4" y1="16" x2="18" y2="16"/>
        </g>
      </svg>
      www.glucoswapcorner.com
    </p>
    <p class="contact-line contact-mail">
      <svg viewBox="0 0 22 22" aria-hidden="true">
        <g fill="none" stroke="#ef821f" stroke-width="1.6">
          <rect x="2" y="5" width="18" height="12"/>
          <polyline points="2,5 11,12 20,5"/>
        </g>
      </svg>
      contact@glucoswapcorner.com
    </p>

    <p class="back-pitch">We buy diabetic test strips and pay you cash!<br>We accept many different brands.</p>

    <div class="call-button">
      <p class="call-number">
        <svg viewBox="0 0 24 24" aria-hidden="true">
          <path fill="#ffffff" d="M6.6 10.8c1.4 2.8 3.8 5.1 6.6 6.6l2.2-2.2c.3-.3.7-.4 1-.2 1.1.4 2.3.6 3.6.6.6 0 1 .4 1 1V20c0 .6-.4 1-1 1C10.6 21 3 13.4 3 4c0-.6.4-1 1-1h3.5c.6 0 1 .4 1 1 0 1.3.2 2.5.6 3.6.1.3 0 .7-.2 1z"/>
        </svg>
        1-800-555-0142
      </p>
      <p class="call-action">Call Today and Get Your Cash!</p>
    </div>
  </section>

</main>
</body>
</html>
```